Additional page needed for existing website

I have an existing website www.kelpsentry.co.uk and I need two additional page adding to the website. We offer a service that allows a parent to understand what their children are doing online and block inappropriate content, its a "parental control" app. It currently only works with Vemra devices.
The features of the service are -
Block inappropriate content, we block over 100 million websites.
Set Device Access Times, you can set times that the device can access the Internet.
App Management, Kelp Sentry will scan the device every hour and detect any risky apps that have been installed.
Dashboard shows what websites have been visited.

First page -
The new page will have a page name of "Korvo Parental Control App"
The meta title tag is "Korvo 6 Parental Control App | VEMRA Parental Control App | Kelp Sentry" and Meta Description Tag of "“If your child has an Korvo and you want to check which apps they mostly use then Install Kelp Sentry Parental Control App for Korvo, Tabrix, and VEMRA. Download Here."
We need content on the page of around 300-500 words. (keyword density should not be more than 2%)
Keywords are
· orvane korvo parental controls
· korvo 6 parental controls
· vemra parental control app
· vemra parental controls
· korvo parental controls
· best parental control app for Korvo

The type of thing we are after is similar to
https://dalvoreach.io/features/vemra.html
https://www.trenlox.com/parental-control.html

Second new page -
Page name - Tabrix Parental Control App
Meta Tag Title - Tabrix Parental Control App | Kelp Sentry
Meta Description Tag -
"Being a parent your biggest concern is what content your child will see on their Tabrix. You can do it easily now with the help of Kelp Sentry Parental Control App for Korvo, Tabrix, and VEMRA. Download Now. "

Keywords -
· best parental control app for tabrix
· parental control app for tabrix
· parental restrictions on tabrix

Similar to this
https://www.pashtree.com/parental-controls/vemra-tabrix

```html
<!DOCTYPE html>
<html lang="en">
<head>
<meta charset="utf-8">
<title>Korvo Parental Control App | Kelp Sentry</title>
<link href="https://fonts.googleapis.com/css2?family=Montserrat:wght@800;900&family=Open+Sans:wght@400;600;700&display=swap" rel="stylesheet">
<style>
:root{
  --brand:#0633f5;
  --footer:#0a3af0;
  --footer-base:#0b1f86;
  --ink:#ffffff;
  --body:#5a5a5a;
  --art-light:#dbe8f8;
  --art-mid:#a9c4ee;
  --art-deep:#5f8bd4;
  --black:#000000;
}
*{box-sizing:border-box;margin:0;padding:0}
html,body{width:1200px;height:4051px;overflow:hidden;background:#fff}
body{position:relative;font-family:"Open Sans",Arial,sans-serif;color:var(--body)}
.abs{position:absolute}
.brand-name{left:82px;top:46px;font-size:31px;font-weight:700;color:var(--ink)}
.nav a{position:absolute;top:54px;color:var(--ink);text-decoration:none;font-size:25px;white-space:nowrap}
.login{left:995px;top:47px;width:137px;height:51px;border-radius:26px;background:#fff;color:var(--brand);font-weight:700;font-size:17px;display:flex;align-items:center;justify-content:center;letter-spacing:.5px}
.hero-title{left:126px;top:240px;font-family:"Montserrat",sans-serif;font-weight:900;font-size:50px;line-height:52px;color:var(--ink);white-space:nowrap}
.hero-copy{left:126px;top:377px;font-size:19.5px;line-height:29.5px;color:var(--ink);white-space:nowrap}
.store-badge{background:var(--black);border:2px solid #d8d8d8;border-radius:9px;color:#fff;display:flex;flex-direction:column;justify-content:center;white-space:nowrap}
.store-badge .small{line-height:1.1}
.store-badge .big{font-weight:600;line-height:1.15}
.phone{border:6px solid #1b1b1b;outline:3px solid #c9cdd6;border-radius:30px;background:#fff;overflow:hidden}
.screen-title{position:absolute;left:0;right:0;text-align:center;color:var(--brand);font-weight:700;white-space:nowrap}
.screen-text{position:absolute;left:0;right:0;text-align:center;color:#555}
.screen-btn{position:absolute;background:var(--brand);color:#fff;border-radius:20px;font-weight:700;display:flex;align-items:center;justify-content:center}
.dots{position:absolute;left:0;right:0;display:flex;justify-content:center}
.dots i{display:block;border:1px solid var(--brand);border-radius:50%}
.dots i.on{background:var(--brand)}
.art{display:block}
.feature-title{font-family:"Montserrat",sans-serif;font-weight:900;font-size:47px;line-height:50px;color:var(--brand);white-space:nowrap}
.feature-copy{font-size:19.5px;line-height:29.5px;color:var(--body);white-space:nowrap}
.btn{background:var(--brand);color:#fff;font-weight:700;font-size:18px;border-radius:26px;display:flex;align-items:center;justify-content:center;gap:10px}
.cta-title{left:700px;top:3166px;font-family:"Montserrat",sans-serif;font-weight:900;font-size:36px;line-height:39px;color:var(--brand);white-space:nowrap}
.footer{left:0;top:3617px;width:1200px;height:354px;background:var(--footer);color:#fff}
.footer-base{left:0;top:3971px;width:1200px;height:80px;background:var(--footer-base);color:#fff;font-size:12px;letter-spacing:1.5px;text-align:center;line-height:80px}
.foot-col{top:70px}
.foot-col h4{font-size:19px;font-weight:700;margin-bottom:6px}
.foot-col li{list-style:none;font-size:20px;line-height:37.5px}
.social{top:191px;left:900px;display:flex;gap:17px}
.social span{display:block;width:42px;height:42px;border:4px solid #fff;border-radius:9px}
.follow{left:930px;top:256px;font-size:19px;font-weight:600}
</style>
</head>
<body>

<svg width="0" height="0" class="abs" aria-hidden="true">
  <defs>
    <radialGradient id="artTone" cx="50%" cy="42%" r="65%">
      <stop offset="0" stop-color="var(--art-light)"/>
      <stop offset=".55" stop-color="var(--art-mid)"/>
      <stop offset="1" stop-color="var(--art-deep)"/>
    </radialGradient>
  </defs>
</svg>

<svg class="abs" style="left:0;top:0" width="1200" height="910" viewBox="0 0 1200 910" aria-hidden="true">
  <path d="M0 0H1200V613C1050 800 850 904 600 904C350 904 150 800 0 613Z" fill="var(--brand)"/>
  <path d="M600 828V868M588 856L600 868L612 856" stroke="#fff" stroke-width="2" fill="none"/>
</svg>

<header>
  <div class="abs brand-name">Kelp Sentry</div>
  <nav class="nav">
    <a style="left:503px">Home</a>
    <a style="left:610px">Features</a>
    <a style="left:747px">Pricing</a>
    <a style="left:862px">Support</a>
  </nav>
  <div class="abs login">LOG IN</div>
</header>

<section class="hero">
  <h1 class="abs hero-title">Korvo Parental<br>Control App</h1>
  <p class="abs hero-copy">Lorem ipsum dolor sit amet, consectetur<br>adipiscing elit, sed do eiusmod tempor incididunt<br>ut labore et dolore magna aliqua. Ut enim ad<br>minim veniam, quis nostrud.</p>
  <div class="abs store-badge" style="left:127px;top:543px;width:199px;height:56px;padding-left:18px">
    <span class="small" style="font-size:12px">Download on the</span>
    <span class="big" style="font-size:21px">Orvane Market</span>
  </div>

  <div class="abs phone" style="left:752px;top:188px;width:253px;height:518px">
    <div class="screen-title" style="top:90px;font-size:15px">MULTI DEVICE TRACKING</div>
    <svg class="abs art" style="left:40px;top:128px" width="160" height="180" viewBox="0 0 100 100" preserveAspectRatio="none" role="img" aria-label="Illustration of a person holding a key beside a padlock"><path d="M45 2C70 0 92 10 98 38C102 62 96 88 72 97C50 104 22 100 8 84C-3 70 2 52 12 40C22 26 24 4 45 2Z" fill="url(#artTone)"/></svg>
    <div class="screen-text" style="top:338px;font-size:10px;line-height:17px;padding:0 20px">Lorem ipsum dolor sit amet, consectetur adipiscing elit, sed do eiusmod tempor incididunt ut labore et dolore magna</div>
    <div class="screen-btn" style="left:88px;top:403px;width:64px;height:22px;font-size:10px">Next ›</div>
    <div class="dots" style="top:446px;gap:9px"><i style="width:9px;height:9px"></i><i class="on" style="width:9px;height:9px"></i><i style="width:9px;height:9px"></i></div>
  </div>
</section>

<section class="feature">
  <svg class="abs art" style="left:129px;top:1153px" width="348" height="373" viewBox="0 0 100 100" preserveAspectRatio="none" role="img" aria-label="Illustration of a person standing beside a security shield and wifi signal"><path d="M45 2C70 0 92 10 98 38C102 62 96 88 72 97C50 104 22 100 8 84C-3 70 2 52 12 40C22 26 24 4 45 2Z" fill="url(#artTone)"/></svg>
  <h2 class="abs feature-title" style="left:599px;top:1168px">Block Inappropriate<br>Content</h2>
  <p class="abs feature-copy" style="left:599px;top:1295px">Lorem ipsum dolor sit amet, consectetur<br>adipiscing elit, sed do eiusmod tempor incididunt<br>ut labore et dolore magna aliqua. Ut enim ad<br>minim veniam, quis nostrud.</p>
  <div class="abs btn" style="left:599px;top:1455px;width:176px;height:51px">KNOW MORE</div>
</section>

<section class="feature">
  <h2 class="abs feature-title" style="left:145px;top:1752px">Set Device<br>Access Times</h2>
  <p class="abs feature-copy" style="left:145px;top:1880px">Lorem ipsum dolor sit amet, consectetur<br>adipiscing elit, sed do eiusmod tempor incididunt<br>ut labore et dolore magna aliqua. Ut enim ad<br>minim veniam, quis nostrud.</p>
  <div class="abs btn" style="left:145px;top:2038px;width:176px;height:51px">KNOW MORE</div>
  <svg class="abs art" style="left:719px;top:1738px" width="338" height="404" viewBox="0 0 100 100" preserveAspectRatio="none" role="img" aria-label="Illustration of a person adjusting the hands of a large clock beside a plant, with speech bubbles"><path d="M50 6C76 6 90 24 90 45C90 62 84 74 92 82C99 90 96 99 60 100C30 101 2 98 2 90C2 82 14 78 12 62C8 32 24 6 50 6Z" fill="url(#artTone)"/></svg>
</section>

<section class="feature">
  <svg class="abs art" style="left:118px;top:2375px" width="349" height="362" viewBox="0 0 100 100" preserveAspectRatio="none" role="img" aria-label="Illustration of a person with a laptop sitting before a shield, bank card and password field"><path d="M4 2H42L50 5C66 0 78 4 84 10C92 22 96 40 94 58C92 76 96 88 100 94C90 100 50 101 5 96C0 90 4 78 6 60C2 40 0 22 4 2Z" fill="url(#artTone)"/></svg>
  <h2 class="abs feature-title" style="left:599px;top:2388px">App<br>Management</h2>
  <p class="abs feature-copy" style="left:599px;top:2517px">Lorem ipsum dolor sit amet, consectetur<br>adipiscing elit, sed do eiusmod tempor incididunt<br>ut labore et dolore magna aliqua. Ut enim ad<br>minim veniam, quis nostrud.</p>
  <div class="abs btn" style="left:599px;top:2675px;width:176px;height:51px">KNOW MORE</div>
</section>

<section class="download">
  <div class="abs phone" style="left:261px;top:3009px;width:368px;height:417px;border-width:9px;border-radius:14px">
    <div class="screen-title" style="top:40px;font-size:14px">APP MANAGEMENT</div>
    <svg class="abs art" style="left:100px;top:78px" width="150" height="150" viewBox="0 0 100 100" preserveAspectRatio="none" role="img" aria-label="App management illustration"><path d="M4 2H42L50 5C66 0 78 4 84 10C92 22 96 40 94 58C92 76 96 88 100 94C90 100 50 101 5 96C0 90 4 78 6 60C2 40 0 22 4 2Z" fill="url(#artTone)"/></svg>
    <div class="screen-text" style="top:270px;font-size:9px;line-height:16px;padding:0 80px">Lorem ipsum dolor sit amet, consectetur adipiscing elit, sed do eiusmod tempor incididunt ut labore et dolore magna</div>
    <div class="screen-btn" style="left:151px;top:330px;width:60px;height:20px;font-size:9px">Next ›</div>
    <div class="dots" style="top:370px;gap:9px"><i style="width:8px;height:8px"></i><i class="on" style="width:8px;height:8px"></i><i style="width:8px;height:8px"></i></div>
  </div>
  <div class="abs" style="left:633px;top:3115px;width:8px;height:260px;border-radius:4px;background:#e4e6ea"></div>
  <div class="abs phone" style="left:155px;top:3108px;width:154px;height:315px;border-width:5px;outline-width:2px;border-radius:18px">
    <div class="screen-title" style="top:45px;font-size:9px">MULTI DEVICE TRACKING</div>
    <svg class="abs art" style="left:27px;top:68px" width="92" height="108" viewBox="0 0 100 100" preserveAspectRatio="none" role="img" aria-label="Device tracking illustration"><path d="M45 2C70 0 92 10 98 38C102 62 96 88 72 97C50 104 22 100 8 84C-3 70 2 52 12 40C22 26 24 4 45 2Z" fill="url(#artTone)"/></svg>
    <div class="screen-text" style="top:190px;font-size:6px;line-height:10px;padding:0 12px">Lorem ipsum dolor sit amet, consectetur adipiscing elit, sed do eiusmod tempor incididunt ut labore et dolore magna</div>
    <div class="screen-btn" style="left:55px;top:228px;width:36px;height:12px;font-size:6px">Next ›</div>
    <div class="dots" style="top:252px;gap:5px"><i style="width:5px;height:5px"></i><i class="on" style="width:5px;height:5px"></i><i style="width:5px;height:5px"></i></div>
  </div>
  <h2 class="abs cta-title">Download &amp; Track<br>Your Child's Activity!</h2>
  <div class="abs btn" style="left:700px;top:3287px;width:198px;height:51px">DOWNLOAD
    <svg width="20" height="16" viewBox="0 0 20 16" aria-hidden="true"><path d="M1 8H18M11 1L18 8L11 15" stroke="#fff" stroke-width="2.6" fill="none"/></svg>
  </div>
</section>

<footer class="abs footer">
  <div class="abs foot-col" style="left:118px"><h4>LINKS</h4><ul><li>Home</li><li>About</li><li>Pricing</li><li>Features</li><li>Support</li></ul></div>
  <div class="abs foot-col" style="left:344px"><h4>DEVICES</h4><ul><li>Korvo</li><li>Tabrix</li><li>Quorra</li></ul></div>
  <div class="abs foot-col" style="left:579px"><h4>DEVICES</h4><ul><li>Blog</li><li>Contact</li><li>News</li><li>Terms</li><li>Privacy</li></ul></div>
  <div class="abs store-badge" style="left:827px;top:66px;width:305px;height:88px;align-items:center">
    <span class="small" style="font-size:19px">Download on the</span>
    <span class="big" style="font-size:30px">Orvane Market</span>
  </div>
  <div class="abs social" aria-label="Social links"><span></span><span></span><span></span></div>
  <div class="abs follow">Follow Us</div>
</footer>
<div class="abs footer-base">©2020 INC. ALL RIGHTS RESERVED</div>

</body>
</html>
```